Bref créative
RL Advisory
I need double sided standard sized Business Card [3.5" x 2"]
Use same font as in logo...also can mix it up with complimentary font
Professional
Romy Lindqvist, MSc, PCC
Portland, OR
rl@romylindqvist-demo.com
www.romylindqvist-demo.com
please add twitter account underneath email address
Twitter: @RLpathways
Symbol only in the middle of the back of card.
with website address noted again underneath the symbol (www.romylindqvist-demo.com)

```html
<!DOCTYPE html>
<html lang="en">
<head>
<meta charset="utf-8">
<title>RL Advisory – Business Cards</title>
<link href="https://fonts.googleapis.com/css2?family=Source+Sans+3:wght@400;600&display=swap" rel="stylesheet">
<style>
  :root {
    --maroon: #6e0a0c;
    --maroon-deep: #650000;
    --ink: #1c1c1c;
    --muted: #333333;
    --card-edge: #c9c9c9;
    --paper: #ffffff;
    --silver-light: #ececec;
    --silver-dark: #a9a9ab;
  }
  * { box-sizing: border-box; margin: 0; padding: 0; }
  html, body {
    width: 1200px; height: 713px; overflow: hidden;
    background: var(--paper);
    font-family: "Source Sans 3", "Myriad Pro", Arial, sans-serif;
  }
  .sheet { position: relative; width: 1200px; height: 713px; }
  .card {
    position: absolute; width: 547px; height: 305px;
    border: 1px solid var(--card-edge);
    overflow: hidden;
  }
  .card--front { left: 29px; top: 36px; background: var(--paper); }
  .card--back-white { left: 612px; top: 36px; background: var(--paper); }
  .card--back-maroon { left: 29px; top: 368px; background: var(--maroon-deep); border-color: var(--maroon-deep); }
  .card--back-silver {
    left: 612px; top: 368px;
    background: radial-gradient(ellipse at center, var(--silver-light) 0%, #d2d2d4 55%, var(--silver-dark) 100%);
  }

  .brand { display: flex; align-items: center; gap: 8px; }
  .brand__dot { width: 13px; height: 13px; border-radius: 50%; background: var(--maroon); flex: none; }
  .brand__name { font-weight: 600; color: var(--ink); line-height: 1; white-space: nowrap; }
  .brand__tagline { font-size: 11px; color: var(--maroon); font-weight: 600; margin-top: 2px; white-space: nowrap; }

  /* front */
  .front__brand { position: absolute; left: 18px; top: 104px; }
  .front__brand .brand__name { font-size: 30px; }
  .front__brand .brand__tagline { margin-left: 58px; font-size: 10.5px; }
  .front__person {
    position: absolute; left: 252px; top: 160px;
    font-size: 19px; color: var(--maroon); white-space: nowrap;
  }
  .front__details {
    position: absolute; left: 18px; top: 200px;
    font-size: 12.5px; line-height: 17.5px; color: var(--muted);
    list-style: none;
  }
  .front__details .web { color: var(--maroon); }

  /* backs */
  .back__center {
    position: absolute; left: 0; right: 0; top: 186px;
    display: flex; flex-direction: column; align-items: center;
  }
  .back__center .brand__name { font-size: 40px; }
  .back__center .brand__tagline { font-size: 12px; margin-left: 70px; }
  .back__web { margin-top: 20px; font-size: 13px; color: var(--ink); }

  .card--back-maroon .brand__name { color: var(--paper); }
  .card--back-maroon .brand__dot { background: var(--paper); }
  .card--back-maroon .brand__tagline { color: var(--paper); }
  .card--back-silver .brand__tagline { color: var(--maroon); }
</style>
</head>
<body>
<main class="sheet">

  <section class="card card--front" aria-label="Card front">
    <div class="front__brand">
      <div class="brand">
        <span class="brand__dot"></span>
        <span class="brand__name">RL Advisory</span>
      </div>
      <div class="brand__tagline">Talent and Career Guidance</div>
    </div>
    <p class="front__person">Romy Lindqvist, MSc, PCC</p>
    <ul class="front__details">
      <li>Portland, OR</li>
      <li>Phone: 615.555.0148</li>
      <li>Email: rl@romylindqvist-demo.com</li>
      <li>Twitter: @RLpathways</li>
      <li class="web">www.romylindqvist-demo.com</li>
    </ul>
  </section>

  <section class="card card--back-white" aria-label="Card back, white">
    <div class="back__center">
      <div class="brand">
        <span class="brand__dot"></span>
        <span class="brand__name">RL Advisory</span>
      </div>
      <div class="brand__tagline">Talent and Career Guidance</div>
      <p class="back__web">www.romylindqvist-demo.com</p>
    </div>
  </section>

  <section class="card card--back-maroon" aria-label="Card back, maroon">
    <div class="back__center">
      <div class="brand">
        <span class="brand__dot"></span>
        <span class="brand__name">RL Advisory</span>
      </div>
      <div class="brand__tagline">Talent and Career Guidance</div>
    </div>
  </section>

  <section class="card card--back-silver" aria-label="Card back, silver">
    <div class="back__center">
      <div class="brand">
        <span class="brand__dot"></span>
        <span class="brand__name">RL Advisory</span>
      </div>
      <div class="brand__tagline">Talent and Career Guidance</div>
      <p class="back__web">www.romylindqvist-demo.com</p>
    </div>
  </section>

</main>
</body>
</html>
```